Letterhead for a German Distribution/Manufacturing Company

We need a professional Letterhead in a unique Design.
not to playful.
The Letterhead has to show show that we are a international company with headquater in Germany.
all details like adress, Vat Tax Number, Bank Accout, Eori, email, Company number has to be on the Letterhead.
for example use: VAT TAX DE5140683 Bank Account: Halmer Kreditbank IBAN DE417052381ß240316 Swift: HKRB0513742 EORI 3150827469 Company Number: HRB 58106 Adress: VOLINTRA UG Tannwiesen Strasse 7 Postal Code 09385 City Burgstädt Country: Germany Email: info@volintra-mail.net
the design can be colored but doesnt have to be
Industry/Entity Type
Manufacturing and international distribution
Requirements
Must have
- show that we are a international company with headquater in Germany. our company infos and logo

```html
<!DOCTYPE html>
<html lang="en">
<head>
<meta charset="utf-8">
<title>Volintra UG Letterhead</title>
<link href="https://fonts.googleapis.com/css2?family=Montserrat:wght@500;600&family=Arimo&display=swap" rel="stylesheet">
<style>
  :root {
    --brand-blue: #2196d3;
    --bar-dark: #333333;
    --ink: #1f1f1f;
    --body-ink: #2e2e2e;
    --paper: #ffffff;
    --backdrop: #ffffff;
    --sign-tone: #d9d9d9;
  }
  * { margin: 0; padding: 0; box-sizing: border-box; }
  html, body { width: 1200px; height: 1200px; overflow: hidden; background: var(--backdrop); }
  .canvas { position: relative; width: 1200px; height: 1200px; }
  .sheet {
    position: absolute; left: 242.5px; top: 136px; width: 722.5px; height: 935px;
    background: var(--paper); overflow: hidden;
    box-shadow: 0 0 60px rgba(0,0,0,0.22);
    font-family: "Montserrat", sans-serif; color: var(--ink);
  }
  .brand-block {
    position: absolute; left: 50.6px; top: 0; width: 149.4px; height: 134.4px;
    background: var(--brand-blue);
    display: flex; align-items: center; justify-content: center; gap: 6px;
  }
  .brand-dot { width: 12px; height: 12px; border-radius: 50%; background: #fff; }
  .brand-name { color: #fff; font-weight: 500; font-size: 14.5px; letter-spacing: 0.3px; }
  .header-bar { position: absolute; left: 200px; top: 101px; width: 522.5px; height: 10.6px; background: var(--bar-dark); }
  .recipient { position: absolute; left: 50.6px; top: 155px; }
  .recipient-to { font-size: 14px; font-weight: 500; line-height: 1.1; }
  .recipient-role { font-size: 10.5px; font-weight: 600; margin-top: 3px; }
  .letter-date { position: absolute; right: 53.75px; top: 193px; font-size: 17px; font-weight: 600; }
  .company-ids { position: absolute; left: 51px; top: 223px; font-size: 13.5px; font-weight: 500; line-height: 16px; }
  .letter-body {
    position: absolute; left: 51px; top: 305px; width: 615.6px;
    font-family: "Arimo", sans-serif; font-size: 15px; line-height: 17.25px; color: var(--body-ink);
  }
  .body-line { display: block; white-space: nowrap; text-align: justify; text-align-last: justify; }
  .body-line.last { text-align-last: left; }
  .spread-line { display: flex; justify-content: space-between; }
  .letter-body .paragraph + .paragraph { margin-top: 34.5px; }
  .signoff { position: absolute; left: 50.6px; top: 685px; font-size: 20px; font-weight: 500; color: var(--bar-dark); }
  .signature-area { position: absolute; left: 51px; top: 712px; width: 114px; height: 17px; background: var(--sign-tone); }
  .footer-band { position: absolute; left: 0; top: 0; width: 722.5px; height: 935px; }
  .footer-country { position: absolute; left: 100.6px; top: 875px; color: #fff; font-size: 25px; font-weight: 500; letter-spacing: 0.5px; }
  .footer-divider { position: absolute; top: 873px; width: 2px; height: 33px; background: #fff; }
  .footer-info { position: absolute; top: 879px; color: #fff; font-size: 9.2px; font-weight: 600; line-height: 13px; white-space: nowrap; }
</style>
</head>
<body>
<div class="canvas">
  <div class="sheet">
    <div class="brand-block">
      <span class="brand-dot"></span>
      <span class="brand-name">VOLINTRA</span>
    </div>
    <div class="header-bar"></div>

    <div class="recipient">
      <div class="recipient-to">TO</div>
      <div class="recipient-role">President / CEO</div>
    </div>
    <div class="letter-date">1, april, 2023</div>

    <div class="company-ids">
      <div>VAT TAX DE5140683</div>
      <div>Halmer Kreditbank IBAN DE417052381ß240316</div>
    </div>

    <div class="letter-body">
      <div class="paragraph">
        <span class="body-line">"Lorem ipsum dolor sit amet, consectetur adipiscing elit, sed do eiusmod tempor incididunt</span>
        <span class="body-line">ut labore et dolore magna aliqua. Ut enim ad minim veniam, quis nostrud exercitation</span>
        <span class="body-line">ullamco laboris nisi ut aliquip ex ea commodo consequat. Duis aute irure dolor in</span>
        <span class="body-line">reprehenderit in voluptate velit esse cillum dolore eu fugiat nulla pariatur. Excepteur sint</span>
        <span class="body-line">occaecat cupidatat non proident, sunt in culpa qui officia deserunt mollit anim id est</span>
        <div class="spread-line"><span>l</span><span>a</span><span>b</span><span>o</span><span>r</span><span>u</span><span>m</span><span>.</span><span>"</span></div>
      </div>
      <div class="paragraph">
        <span class="body-line">"Sed ut perspiciatis unde omnis iste natus error sit voluptatem accusantium doloremque</span>
        <span class="body-line">laudantium, totam rem aperiam, eaque ipsa quae ab illo inventore veritatis et quasi</span>
        <span class="body-line">architecto beatae vitae dicta sunt explicabo. Nemo enim ipsam voluptatem quia voluptas</span>
        <span class="body-line">sit aspernatur aut odit aut fugit, sed quia consequuntur magni dolores eos qui ratione</span>
        <span class="body-line">voluptatem sequi nesciunt. Neque porro quisquam est, qui dolorem ipsum quia dolor sit</span>
        <span class="body-line">amet, consectetur, adipisci velit, sed quia non numquam eius modi tempora incidunt ut</span>
        <span class="body-line">labore et dolore magnam aliquam quaerat voluptatem. Ut enim ad minima veniam, quis</span>
        <span class="body-line">nostrum exercitationem ullam corporis suscipit laboriosam, nisi ut aliquid ex ea commodi</span>
        <span class="body-line">consequatur? Quis autem vel eum iure reprehenderit qui in ea voluptate velit esse quam</span>
        <span class="body-line last">nihil molestiae consequatur, vel illum qui dolorem eum fugiat quo voluptas nulla pariatur?"</span>
      </div>
    </div>

    <div class="signoff">Director</div>
    <div class="signature-area" role="img" aria-label="Handwritten signature of the director"></div>

    <svg class="footer-band" viewBox="0 0 722.5 935" aria-hidden="true">
      <polygon points="0,871 722.5,749.4 722.5,935 0,935" fill="var(--brand-blue)"/>
    </svg>
    <div class="footer-country">GERMANY</div>
    <div class="footer-divider" style="left:257.5px"></div>
    <div class="footer-info" style="left:277.5px">VOLINTRA UG Tannwiesen Strasse 7 Postal<br>HKRB0513742 EORI 3150827469</div>
    <div class="footer-divider" style="left:495.6px"></div>
    <div class="footer-info" style="left:525px">HRB 58106<br>info@volintra-mail.net</div>
  </div>
</div>
</body>
</html>
```